Poster for Wobble Evening - a weekly comedy/variety show

We would like a poster/postcard design for a weekly alternative comedy/variety show called Wobble Evening.
Style: The poster should be fun and eye catching and very bold. It should have an alternative feel, not mainstream. Weird, strange, bizarre and funny is good. The show's title "Wobble Evening" should be very prominent. I like the idea of it being busy and cartoony, a collage of weirdness. Fenwick Dabble's Spinning Carnival or Cpt. Quimby's Restless Ankle's Parade Troupe or psychedelic rock posters of the 70's.
Design Specifics: We are looking for one design that can both be on an 11" x 17" poster and reduced to a 4" x 6" postcard.
The copy:
-
vtm productions presents:
Wobble Evening
standup, music, storytelling, sketch and improv
Wednesdays @ Gullfeather Theatre
5164 W. Larkmont - 2nd Floor
Chicago, IL 60588
7:30 - The Loose Hour
8:30 - The Medley Hour
9:45 - Torbeck Ladder
Pay what you want
website: wobbleevening.example
-
The back of the postcard can be very simple. We may add stickers to it regularly with the specific dates and the names of guest performers.
UPDATE: I've updated the copy a little bit and made this a guaranteed contest.
Reason: I asked a couple designers to submit changes and have extended the deadline so that they have time to do that.
I have picked a design and I'm just now going to try to choose between the variations of that poster that the designer posted. No need to add any more designs unless I request them directly.
Young adults (20s-40s), college students, living on the north side of Chicago who are looking for a fun, inexpensive, cool night out during the week.
Club

```html
<!DOCTYPE html>
<html lang="en">
<head>
<meta charset="utf-8">
<title>Wobble Evening — Poster</title>
<link rel="stylesheet" href="https://fonts.googleapis.com/css2?family=Alfa+Slab+One&family=Sorts+Mill+Goudy:ital@1&family=Titillium+Web:wght@700&family=Cormorant+SC:wght@600&family=Cormorant+Garamond:wght@700&display=swap">
<style>
  :root {
    --page: #ffffff;
    --edge: #c8c8c8;
    --ink: #1d1d1d;
    --green: #6aab4e;
    --red-text: #c8262b;
    --magenta: #c8068a;
    --sky: #62adeb;
    --yellow: #f6ea3a;
    --bar-red: #d0222b;
    --fur-dark: #5e4030;
    --fur-mid: #8c6a50;
    --fur-light: #c9ab8e;
  }
  * { margin: 0; padding: 0; box-sizing: border-box; }
  html, body { width: 1200px; height: 1000px; overflow: hidden; background: var(--page); }
  .poster {
    position: absolute; left: 323px; top: 37px; width: 592px; height: 914px;
    border: 1px solid var(--edge); background: var(--page); overflow: hidden;
  }
  .layer { position: absolute; left: 0; top: 0; width: 592px; height: 914px; }
  .presenter {
    position: absolute; left: 52px; top: 110px; width: 120px;
    font: 700 14px/18px "Titillium Web", sans-serif; color: var(--ink); text-transform: uppercase; letter-spacing: .3px;
  }
  .venue {
    position: absolute; left: 351px; top: 54px; width: 221px; text-align: center;
    font-family: "Cormorant SC", serif; color: var(--red-text);
  }
  .venue .day { font: italic 26px/32px "Sorts Mill Goudy", serif; }
  .venue .place { font-size: 18px; line-height: 32px; letter-spacing: 1px; font-weight: 600; }
  .venue .addr { font-size: 16px; line-height: 32px; font-weight: 600; }
  .acts {
    position: absolute; left: 32px; top: 318px; width: 86px; list-style: none;
    font: 600 12px/25.5px "Cormorant SC", serif; color: var(--magenta); letter-spacing: .8px; text-transform: lowercase;
  }
  .schedule { position: absolute; left: 266px; top: 552px; color: var(--yellow); font-family: "Cormorant Garamond", serif; font-weight: 700; }
  .slot .time { display: block; font-size: 66px; line-height: 62px; }
  .slot .show { display: block; font-size: 29px; line-height: 32px; margin-bottom: 10px; white-space: nowrap; }
  .pay {
    position: absolute; left: 52px; top: 750px;
    font: 700 20px/24px "Titillium Web", sans-serif; color: var(--ink); text-transform: uppercase;
  }
  .site {
    position: absolute; left: 0; top: 843px; width: 240px; height: 34px; background: var(--bar-red);
    color: #fff; font: 700 14px/34px "Titillium Web", sans-serif; padding-left: 28px; white-space: nowrap;
  }
</style>
</head>
<body>
<main class="poster">
  <svg class="layer backdrop" viewBox="0 0 592 914">
    <defs>
      <linearGradient id="fur" x1="0" y1="0" x2="1" y2="1">
        <stop offset="0" stop-color="var(--fur-mid)"/>
        <stop offset=".45" stop-color="var(--fur-dark)"/>
        <stop offset=".8" stop-color="var(--fur-mid)"/>
        <stop offset="1" stop-color="var(--fur-light)"/>
      </linearGradient>
    </defs>
    <path role="img" aria-label="Close-up photograph of a camel's head filling the right of the poster"
      d="M60 200 C80 170 160 175 260 140 C350 110 480 110 592 110 L592 914 L70 914 C40 860 30 780 60 700 C80 640 40 560 30 480 C20 380 30 260 60 200 Z"
      fill="url(#fur)"/>
    <rect class="venue-card" x="351" y="49" width="221" height="212" fill="var(--green)"/>
    <rect class="title-accent" x="21" y="296" width="110" height="222" fill="var(--sky)"/>
  </svg>

  <p class="presenter">vtm productions presents:</p>

  <div class="venue">
    <p class="day">Wednesdays</p>
    <p class="place">@ Gullfeather<br>Theatre</p>
    <p class="addr">5164 W. Larkmont -<br>2nd Floor<br>Chicago, IL 60588</p>
  </div>

  <svg class="layer title" viewBox="0 0 592 914">
    <text x="124" y="382" textLength="460" lengthAdjust="spacingAndGlyphs"
      font-family="'Alfa Slab One', serif" font-size="150" fill="#fff">W<tspan fill="var(--magenta)">O</tspan>BBLE</text>
    <text x="124" y="542" textLength="460" lengthAdjust="spacingAndGlyphs"
      font-family="'Alfa Slab One', serif" font-size="150" fill="#fff">EVENING</text>
  </svg>

  <ul class="acts">
    <li>standup,</li><li>music,</li><li>story-</li><li>telling,</li><li>sketch</li><li>and</li><li>improv</li>
  </ul>

  <div class="schedule">
    <p class="slot"><span class="time">7:30</span><span class="show">The Loose Hour</span></p>
    <p class="slot"><span class="time">8:30</span><span class="show">The Medley Hour</span></p>
    <p class="slot"><span class="time">9:45</span><span class="show">Torbeck Ladder</span></p>
  </div>

  <p class="pay">Pay what<br>you want</p>
  <p class="site">website: wobbleevening.example</p>
</main>
</body>
</html>
```